Alternative Health business needs a self help book cover design

Silver Brook Wellness requires an E book and print cover design for a new self help book titled "Making The Bright Choice". Sub title 'Ways to shape the bright days YOU seek' . Author Danica Forworth. The book is about deliberately changing things now, so you feel happy now and this then flows out an effects everything else in your life. It combines NLP, yoga philosophy and modern psychology in a down to earth, easy to read manner. I would like the cover to be happy, colourful, beautiful, artistic and hip. Maybe something hand drawn or painted. Something a woman would want to display and something that makes you smile and feel happy.
I don't want it to look like a romance novel and would prefer no photos of people. Pics are of other peoples covers I like. Thank you in advance. danica

Target Market(s)

woman 18-50

Industry/Entity Type

Business

Requirements
Must have
• happy feeling. professional look
Nice to have
• original drawing or painting
Should not have
• photos of real people, yellow smiley faces, sunsets, butterflies, yoga, tree, elements of my business logo

```html
<!DOCTYPE html>
<html lang="en">
<head>
<meta charset="utf-8">
<title>Making The Bright Choice – Book Cover</title>
<link rel="stylesheet" href="https://fonts.googleapis.com/css2?family=Oswald:wght@300;400;500&display=swap">
<style>
  :root {
    --stage: #7d6a6c;
    --cover-dark: #0b140a;
    --cover-deep: #050a05;
    --title-white: #ffffff;
    --title-green: #3fe51d;
    --subtitle: #f2f2f2;
    --rule: #d9d9d9;
    --art-green: #5fd21e;
    --art-gold: #f0b43a;
    --art-ember: #c4461c;
  }

  * { margin: 0; padding: 0; box-sizing: border-box; }

  html, body {
    width: 1200px;
    height: 909px;
    overflow: hidden;
    background: var(--stage);
  }

  .canvas {
    position: relative;
    width: 1200px;
    height: 909px;
  }

  .book-cover {
    position: absolute;
    left: 330px;
    top: 51px;
    width: 540px;
    height: 807px;
    background: radial-gradient(ellipse at 50% 28%, #1a1a0c 0%, var(--cover-dark) 45%, var(--cover-deep) 100%);
    overflow: hidden;
    font-family: "Oswald", "Arial Narrow", sans-serif;
    text-align: center;
  }

  .cover-art {
    position: absolute;
    left: 33px;
    top: 44px;
    width: 474px;
    height: 306px;
    border-radius: 50% 50% 18% 18% / 60% 60% 20% 20%;
    background:
      radial-gradient(ellipse at 50% 42%, rgba(255, 236, 170, 0.9) 0%, rgba(240, 180, 58, 0.75) 22%, rgba(196, 70, 28, 0.55) 45%, transparent 70%),
      radial-gradient(ellipse at 50% 30%, var(--art-green) 0%, rgba(95, 210, 30, 0.6) 45%, transparent 72%);
    filter: blur(2px);
  }

  .title {
    position: absolute;
    left: 0;
    width: 100%;
    white-space: nowrap;
    font-weight: 500;
    line-height: 1;
    text-transform: uppercase;
  }

  .title-line-one {
    top: 372px;
    font-size: 98px;
    color: var(--title-white);
  }

  .title-line-two {
    top: 494px;
    font-size: 76px;
    color: var(--title-green);
  }

  .subtitle {
    position: absolute;
    left: 0;
    top: 622px;
    width: 100%;
    white-space: nowrap;
    font-weight: 400;
    font-size: 27px;
    line-height: 1;
    color: var(--subtitle);
  }

  .subtitle-emphasis {
    color: var(--title-green);
    font-weight: 500;
  }

  .divider {
    position: absolute;
    left: 62px;
    top: 698px;
    width: 416px;
    height: 2px;
  }

  .author {
    position: absolute;
    left: 0;
    top: 718px;
    width: 100%;
    font-weight: 300;
    font-size: 40px;
    line-height: 1;
    color: var(--title-white);
  }
</style>
</head>
<body>
<main class="canvas">
  <section class="book-cover">
    <div class="cover-art" role="img" aria-label="Glowing illustration of a tree with green and golden leaves above a seated meditating figure"></div>

    <h1>
      <span class="title title-line-one">Making The</span>
      <span class="title title-line-two">Bright Choice</span>
    </h1>

    <p class="subtitle">Ways to shape the bright days <span class="subtitle-emphasis">YOU</span> seek</p>

    <svg class="divider" viewBox="0 0 416 2" preserveAspectRatio="none" aria-hidden="true">
      <defs>
        <linearGradient id="divider-fade" x1="0" x2="1" y1="0" y2="0">
          <stop offset="0" stop-color="#d9d9d9" stop-opacity="0"/>
          <stop offset="0.5" stop-color="#d9d9d9" stop-opacity="1"/>
          <stop offset="1" stop-color="#d9d9d9" stop-opacity="0"/>
        </linearGradient>
      </defs>
      <rect x="0" y="0" width="416" height="2" fill="url(#divider-fade)"/>
    </svg>

    <p class="author">Danica Forworth</p>
  </section>
</main>
</body>
</html>
```